Pre-workout label and Super Greens label for Vantora Nutrition Supplements

I need a label design for Club Vantora's 2 supplements. The first is a Pre-workout. The Pre-workout label needs to be 11.25 x 2.5 inches. This label will go on a black container. The second is a Super-Green. The Super-Green label should be 11.25 x 4.25 inches and will go on a white container. We have been selling these for a few years but the current labels are a little meh. I'd like something trendier and bolder. Must keep the Club Vantora branding. All the nurtition data must appear . I attached the current designs so you can know the flavors, nutrtional data etc. Thank you!
Updates

I can upload the Club Vantora logo! If anyone can tell me how to do that.

```html
<!DOCTYPE html>
<html lang="en">
<head>
<meta charset="utf-8">
<title>Vantora Nutrition – Pre-Workout Label</title>
<link href="https://fonts.googleapis.com/css2?family=Arimo:wght@400;700&family=Oswald:wght@400;500;600&family=Saira:wght@300&display=swap" rel="stylesheet">
<style>
  :root {
    --stage: #cccccc;
    --label-red: #d93d3d;
    --label-dark: #332e31;
    --divider-grey: #a9a7a8;
    --ink-white: #ffffff;
    --ink-black: #1d1b1c;
    --trim-line: #d22fd6;
    --font-body: "Arimo", Arial, sans-serif;
    --font-condensed: "Oswald", "Arial Narrow", sans-serif;
    --font-display: "Saira", "Arial", sans-serif;
  }
  html, body {
    margin: 0;
    width: 1200px;
    height: 1000px;
    overflow: hidden;
    background: var(--stage);
  }
  .stage {
    position: relative;
    width: 1200px;
    height: 1000px;
  }
  .label {
    position: absolute;
    left: 601px;
    top: 499px;
    width: 1260px;
    height: 294px;
    margin-left: -630px;
    margin-top: -147px;
    transform: rotate(-36deg);
    overflow: hidden;
    background: var(--label-red);
    font-family: var(--font-body);
    color: var(--ink-white);
  }
  .label-art {
    position: absolute;
    inset: 0;
  }
  .tilted {
    position: absolute;
    transform: translate(-50%, -50%) rotate(-30deg);
    white-space: nowrap;
    text-align: center;
  }

  /* left panel */
  .usage-box {
    position: absolute;
    left: 37px;
    top: 31px;
    width: 258px;
    height: 188px;
    box-sizing: border-box;
    border: 1px solid var(--ink-white);
    border-radius: 14px;
    padding: 10px 10px;
    font-size: 6.3px;
    line-height: 1.42;
  }
  .usage-box p { margin: 0 0 5px; }
  .usage-box b { font-weight: 700; }
  .fda-note {
    position: absolute;
    left: 33px;
    top: 230px;
    width: 265px;
    height: 34px;
    box-sizing: border-box;
    border: 1px solid var(--ink-white);
    border-radius: 17px;
    padding: 6px 14px;
    font-size: 5.6px;
    font-weight: 700;
    line-height: 1.35;
    text-align: center;
  }

  /* brand */
  .brand {
    left: 520px;
    top: 78px;
    display: flex;
    align-items: center;
    gap: 7px;
  }
  .brand-mark {
    width: 11px;
    height: 11px;
    background: var(--ink-white);
  }
  .brand-name {
    font-family: var(--font-condensed);
    font-weight: 500;
    font-size: 14px;
    letter-spacing: 1.2px;
  }

  /* product naming */
  .product-title {
    left: 604px;
    top: 122px;
    font-family: var(--font-display);
    font-weight: 300;
    font-size: 39px;
    letter-spacing: 1px;
    color: var(--label-red);
  }
  .flavor {
    left: 562px;
    top: 186px;
    font-family: var(--font-condensed);
    font-weight: 600;
    font-size: 16px;
    letter-spacing: 1.3px;
  }
  .net-contents {
    left: 608px;
    top: 240px;
    font-family: var(--font-condensed);
    font-weight: 500;
    font-size: 8.5px;
    letter-spacing: 0.8px;
    line-height: 1.8;
  }

  /* benefit badges */
  .benefit {
    display: flex;
    align-items: center;
    gap: 4px;
  }
  .benefit svg { width: 17px; height: 19px; }
  .benefit-text {
    text-align: left;
    font-size: 5.6px;
    line-height: 1.25;
  }
  .benefit-text b {
    display: block;
    font-family: var(--font-condensed);
    font-weight: 600;
    font-size: 6.4px;
    letter-spacing: 0.5px;
  }

  /* supplement facts */
  .facts-panel {
    position: absolute;
    left: 905px;
    top: 16px;
    width: 322px;
    height: 184px;
    box-sizing: border-box;
    background: var(--ink-white);
    color: var(--ink-black);
    padding: 4px 6px;
    font-size: 6.2px;
    line-height: 1.15;
  }
  .facts-title {
    font-weight: 700;
    font-size: 12px;
    line-height: 1.05;
  }
  .facts-serving { border-bottom: 4px solid var(--ink-black); padding-bottom: 1px; }
  .facts-row {
    display: grid;
    grid-template-columns: 1fr 118px 24px;
    border-bottom: 0.6px solid var(--ink-black);
    padding: 0.9px 0;
  }
  .facts-row .dv { text-align: right; }
  .facts-row.head { border-bottom: 2px solid var(--ink-black); }
  .facts-row.heavy { border-bottom: 2.5px solid var(--ink-black); }
  .facts-foot { padding-top: 1px; }

  .ingredients {
    position: absolute;
    left: 905px;
    top: 206px;
    width: 330px;
    font-size: 6.4px;
    line-height: 1.45;
  }
  .ingredients p { margin: 0 0 5px; }
  .ingredients b { font-weight: 700; }
</style>
</head>
<body>
<main class="stage">
  <section class="label" aria-label="Vantora Nutrition Pre-Workout label, Watermelon Sugar">
    <svg class="label-art" width="1260" height="294" viewBox="0 0 1260 294" aria-hidden="true">
      <path class="divider-band" d="M 782 -6 L 482 166 Q 452 183 452 216 L 452 300" fill="none" stroke="var(--divider-grey)" stroke-width="12"/>
      <path class="dark-field" d="M 792 0 L 1260 0 L 1260 294 L 462 294 L 462 216 Q 462 188 490 172 Z" fill="var(--label-dark)"/>
      <path class="benefit-band" d="M 700 294 L 700 106 Q 700 80 726 80 L 746 80 Q 770 80 770 104 L 770 294 Z" fill="var(--label-red)"/>
      <path class="contents-panel" d="M 540 294 L 540 230 Q 540 214 554 206 L 650 150 Q 678 136 678 166 L 678 294 Z" fill="var(--label-red)"/>
      <rect class="trim-guide" x="12" y="12" width="1236" height="270" fill="none" stroke="var(--trim-line)" stroke-width="0.8"/>
    </svg>

    <div class="usage-box">
      <p><b>Directions:</b> Use on training days only. Mix 1 scoop with 6-8 oz of cold water 15-30 minutes prior to training.</p>
      <p><b>Warning:</b> Not intended for use by persons under age 18. Do not exceed recommended dose. Do not consume synephrine or caffeine from other sources, including but not limited to: coffee, tea, soda, and other dietary supplements or medications containing phenylephrine or caffeine. Contains caffeine. Use in a 12 week on, 2 week off pattern. Consult your physician prior to use if you are pregnant or nursing, or if you are taking medication, including but not limited to: MAOI inhibitors, antidepressants, aspirin, non-steroidal, anti-inflammatory drugs or products containing phenylephrine, ephedrine, pseudoephedrine, or other stimulants. Consult your physician prior to use if you have a medical condition, including but not limited to: heart, liver, kidney, or thyroid disease, cardiac arrhythmia, recurrent headaches, enlarged prostate or glaucoma. Discontinue use 2 weeks prior to surgery or if you experience rapid heartbeat, dizziness, severe headaches, or shortness of breath. This product DOES NOT contain ingredients banned by certain sports organizations.</p>
    </div>
    <div class="fda-note">*These statements have not been evaluated by the Food and Drug Administration. This product is not intended to diagnose, treat, cure or prevent any disease.</div>

    <div class="tilted brand">
      <span class="brand-mark"></span>
      <span class="brand-name">VANTORA NUTRITION</span>
    </div>

    <div class="tilted product-title">PRE-WORKOUT</div>
    <div class="tilted flavor">WATERMELON SUGAR</div>
    <div class="tilted net-contents">DIETARY SUPPLEMENT<br>30 SERVINGS 240g (8.5oz)</div>

    <div class="tilted benefit" style="left:742px; top:106px;">
      <svg viewBox="0 0 17 19"><path d="M1 1 H16 V12 L8.5 18 L1 12 Z" fill="none" stroke="#fff" stroke-width="1.4"/><path d="M9.5 4 L5.5 10 H8.5 L7.5 15 L11.5 8.5 H8.5 Z" fill="#fff"/></svg>
      <span class="benefit-text"><b>ENERGY*</b>(Caffeine)</span>
    </div>
    <div class="tilted benefit" style="left:744px; top:158px;">
      <svg viewBox="0 0 17 19"><path d="M1 1 H16 V12 L8.5 18 L1 12 Z" fill="none" stroke="#fff" stroke-width="1.4"/><path d="M8.5 4 L13 9 H10.3 V14 H6.7 V9 H4 Z" fill="#fff"/></svg>
      <span class="benefit-text"><b>PERFORMANCE*</b>(Beta-alanine)</span>
    </div>
    <div class="tilted benefit" style="left:742px; top:212px;">
      <svg viewBox="0 0 17 19"><path d="M1 1 H16 V12 L8.5 18 L1 12 Z" fill="none" stroke="#fff" stroke-width="1.4"/><path d="M4 7 V12 M6 6 V13 M11 6 V13 M13 7 V12 M6 9.5 H11" stroke="#fff" stroke-width="1.5" fill="none"/></svg>
      <span class="benefit-text"><b>STRENGTH*</b>(Creatine)</span>
    </div>

    <div class="facts-panel">
      <div class="facts-title">Supplement Facts</div>
      <div class="facts-serving">Serving Size: 1 Scoop (8 g)<br>Servings per Container: 30</div>
      <div class="facts-row head"><span></span><span>Amount per Serving</span><span class="dv">%DV</span></div>
      <div class="facts-row"><span>Vitamin C (Ascorbic Acid)</span><span>250mg</span><span class="dv">278%</span></div>
      <div class="facts-row"><span>Vitamin B6 (as Pyridoxal-5-Phosphate)</span><span>0.035 mg</span><span class="dv">2%</span></div>
      <div class="facts-row"><span>Folate</span><span>250 mcg DFE (150 mcg Folic Acid)</span><span class="dv">63%</span></div>
      <div class="facts-row"><span>Vitamin B12 (as Methylcobalamin)</span><span>20 mcg</span><span class="dv">833%</span></div>
      <div class="facts-row heavy"><span>Calcium (as Calcium Silicate)</span><span>18.30 mg</span><span class="dv">1%</span></div>
      <div class="facts-row"><span>Beta-Alanine</span><span>1.5 g</span><span class="dv">†</span></div>
      <div class="facts-row"><span>Creatine Monohydrate</span><span>1 g</span><span class="dv">†</span></div>
      <div class="facts-row"><span>L-Arginine Alpha-Ketoglutarate</span><span>1 g</span><span class="dv">†</span></div>
      <div class="facts-row"><span>L-Citrulline Malate</span><span>1 g</span><span class="dv">†</span></div>
      <div class="facts-row"><span>N-Acetyl L-Tyrosine</span><span>500 mg</span><span class="dv">†</span></div>
      <div class="facts-row"><span>Caffeine Anhydrous</span><span>250 mg</span><span class="dv">†</span></div>
      <div class="facts-row heavy"><span>Synephrine HCl</span><span>30 mg</span><span class="dv">†</span></div>
      <div class="facts-foot">† Daily Value (DV) not established</div>
    </div>

    <div class="ingredients">
      <p><b>Other Ingredients:</b> Citric Acid, Pineapple Fruit Juice Powder, Silicon Dioxide, Natural and Artificial Flavors, Acesulfame Potassium, Sucralose, and FD&amp;C Red #40.</p>
      <p><b>Formulated by:</b> Club Vantora, 482 Ridge Rd, Cody, WY 82414 (307) 555-0148</p>
    </div>
  </section>
</main>
</body>
</html>
```